Tobias Webpage Design

I would like to start an business and management consultancy business. I am thinking to called it "Krelto Consultancy". Besides the consultancy services, I would also like to provide training on finance, forensic accounting, fraud prevention and internal control.
Professional management consultants are contracted by organizations to provide advisory services in an objective and independent manner.

Services include, but are not limited to, strategic planning, facilitation, quality assurance, education and training, investment counsel, identification and analysis of management problems, developing solutions, and the implementation of proposed solutions.

Professional management consultants are hired when an organization lacks sufficient resources, requires external objective advice, or because they have expertise not available within the client organization.

I would like to see the webpage design that use colors apple green with some other contrast color. The design have to be professional look but with a new age touch.

Reason: Unable to find a suitable web pages design

Dear all

Since last week I post a request, but till to date, I has yet to received a new sparkling creative and "wow" web page design. Please help me here!

Regards

Reason: Yet to found a suitable web designer for my web design. Help! I just need a fresh and professional look design. You may ignore the color code I prefer. Send me your sparkling creative work. Thank you so much!

Some examples

```html
<!DOCTYPE html>
<html lang="en">
<head>
<meta charset="utf-8">
<title>Krelto Consultancy</title>
<link rel="stylesheet" href="https://fonts.googleapis.com/css2?family=Questrial&display=swap">
<style>
  :root {
    --green: #84bd32;
    --green-dark: #6aa51f;
    --black: #000000;
    --white: #ffffff;
    --ink: #111111;
    --grey-text: #8a8a8a;
  }
  * { margin: 0; padding: 0; box-sizing: border-box; }
  html, body { width: 814px; height: 1200px; overflow: hidden; background: var(--green); }
  body { font-family: "Questrial", "Century Gothic", sans-serif; color: var(--white); }
  .page { position: relative; width: 814px; height: 1200px; overflow: hidden; }
  .band { position: absolute; left: 0; width: 814px; }
  .band--hero { top: 0; height: 418px; background: var(--green); }
  .band--welcome { top: 418px; height: 251px; background: var(--black); }
  .band--field { top: 669px; height: 290px; background: var(--green); }
  .band--contact { top: 959px; height: 241px; background: var(--black); }
  .shapes { position: absolute; left: 0; top: 0; width: 814px; height: 1200px; }
  .t { position: absolute; white-space: nowrap; line-height: 1; }

  .brand { position: absolute; left: 84px; top: -72px; width: 152px; height: 152px; border-radius: 50%; background: var(--black); }
  .brand__name { position: absolute; left: 0; width: 152px; top: 100px; text-align: center; font-size: 14px; color: var(--green); letter-spacing: 0.5px; line-height: 1.2; }

  .nav__item { font-size: 18.5px; color: var(--ink); letter-spacing: 0.3px; }
  .tagline { font-size: 22px; line-height: 27px; color: var(--white); }

  .title { font-size: 34px; letter-spacing: 0.3px; }
  .title em { font-style: normal; color: var(--green); }
  .body-copy { font-size: 15.5px; line-height: 22.3px; }

  .field-title { font-size: 34px; color: var(--ink); }
  .field-item { font-size: 16px; color: var(--white); letter-spacing: 0.3px; }

  .btn-label { font-size: 23px; line-height: 19px; text-align: center; width: 84px; color: var(--white); }

  .form-title { font-size: 18px; color: var(--ink); width: 244px; text-align: center; }
  .field-box { position: absolute; left: 539px; width: 140px; height: 22px; background: var(--white); color: var(--grey-text); font-size: 15px; line-height: 22px; text-align: center; }
  .privacy { font-size: 6.5px; line-height: 8px; color: var(--ink); white-space: normal; width: 120px; }
  .copyright { font-size: 7px; color: var(--white); }
</style>
</head>
<body>
<div class="page">
  <div class="band band--hero"></div>
  <div class="band band--welcome"></div>
  <div class="band band--field"></div>
  <div class="band band--contact"></div>

  <svg class="shapes" viewBox="0 0 814 1200">
    <defs>
      <radialGradient id="hero-tone" cx="55%" cy="45%" r="65%">
        <stop offset="0" stop-color="#f2efe8"/>
        <stop offset="0.6" stop-color="#d9cfbd"/>
        <stop offset="1" stop-color="#b9ad98"/>
      </radialGradient>
      <filter id="soft-shadow" x="-30%" y="-30%" width="160%" height="160%">
        <feDropShadow dx="4" dy="5" stdDeviation="5" flood-color="#000" flood-opacity="0.55"/>
      </filter>
    </defs>

    <!-- nav rail -->
    <line x1="98" y1="128" x2="98" y2="276" stroke="var(--white)" stroke-width="2" stroke-dasharray="4 5"/>
    <circle cx="98" cy="119" r="9.5" fill="var(--black)" stroke="var(--white)" stroke-width="3"/>
    <circle cx="98" cy="160" r="10" fill="var(--green)" stroke="var(--black)" stroke-width="3"/>
    <circle cx="98" cy="202" r="10" fill="var(--green)" stroke="var(--black)" stroke-width="3"/>
    <circle cx="98" cy="243" r="10" fill="var(--green)" stroke="var(--black)" stroke-width="3"/>
    <circle cx="98" cy="284" r="10" fill="var(--green)" stroke="var(--black)" stroke-width="3"/>

    <!-- hero illustration area -->
    <circle cx="548" cy="212" r="184" fill="url(#hero-tone)" role="img" aria-label="Illustration: a magnifying glass showing consultants meeting around a table with a laptop and documents"/>

    <!-- welcome read-more -->
    <line x1="688" y1="427" x2="688" y2="556" stroke="var(--green)" stroke-width="2.5" stroke-dasharray="6 5"/>
    <circle cx="688" cy="418" r="9" fill="var(--black)" stroke="var(--green)" stroke-width="3"/>
    <circle cx="688" cy="599" r="42" fill="var(--black)" stroke="var(--green)" stroke-width="3" filter="url(#soft-shadow)"/>

    <!-- field read-more -->
    <line x1="126" y1="676" x2="126" y2="846" stroke="var(--black)" stroke-width="2.5" stroke-dasharray="6 5"/>
    <circle cx="126" cy="667" r="9" fill="var(--black)" stroke="var(--green)" stroke-width="3"/>
    <circle cx="126" cy="889" r="42" fill="var(--green)" stroke="var(--black)" stroke-width="3" filter="url(#soft-shadow)"/>

    <!-- plus mark -->
    <g fill="var(--green-dark)" filter="url(#soft-shadow)">
      <rect x="397" y="836" width="30" height="88"/>
      <rect x="368" y="865" width="88" height="30"/>
    </g>

    <!-- query form disc -->
    <circle cx="607" cy="1072" r="122" fill="var(--green)" filter="url(#soft-shadow)"/>
    <!-- lock icon -->
    <rect x="544" y="1084" width="10" height="8" rx="1" fill="var(--black)"/>
    <path d="M546 1084 v-3 a3 3 0 0 1 6 0 v3" fill="none" stroke="var(--black)" stroke-width="1.6"/>
    <!-- submit -->
    <circle cx="607" cy="1150" r="42" fill="var(--black)" stroke="var(--green)" stroke-width="3" filter="url(#soft-shadow)"/>
  </svg>

  <div class="brand"><div class="brand__name">Krelto<br>Consultancy</div></div>

  <nav>
    <span class="t nav__item" style="left:124px;top:111px;">HOME</span>
    <span class="t nav__item" style="left:124px;top:152px;">ABOUT</span>
    <span class="t nav__item" style="left:124px;top:194px;">SERVICES</span>
    <span class="t nav__item" style="left:124px;top:235px;">CONTACT</span>
    <span class="t nav__item" style="left:124px;top:276px;">ARTICLES &amp; INFORMATION</span>
  </nav>

  <p class="t tagline" style="left:86px;top:344px;">With Krelto,<br>it is more than just a solution</p>

  <h1 class="t title" style="left:86px;top:460px;">Welcome to <em>Krelto CONSULTANCY</em></h1>
  <p class="t body-copy" style="left:86px;top:530px;">Lorem ipsum dolor sit amet, consectetur adipisicing elit, sed do<br>eiusmod tempor incididunt ut labore et dolore magna aliqua.<br>Ut enim ad minim veniam, quis nostrud exercitation ullamco<br>laboris nisi ut aliquip ex ea commodo consequat.</p>
  <span class="t btn-label" style="left:646px;top:580px;">read<br>more</span>

  <h2 class="t field-title" style="right:84px;top:700px;">Our field</h2>
  <ul style="list-style:none;">
    <li class="t field-item" style="left:213px;top:755px;">strategic planning</li>
    <li class="t field-item" style="left:416px;top:755px;">investment counsel</li>
    <li class="t field-item" style="left:634px;top:755px;">facilitation</li>
    <li class="t field-item" style="left:286px;top:791px;">education and training</li>
    <li class="t field-item" style="left:531px;top:791px;">quality assurance</li>
    <li class="t field-item" style="left:251px;top:874px;">identification</li>
    <li class="t field-item" style="left:224px;top:904px;">developing solutions</li>
    <li class="t field-item" style="left:469px;top:872px;">analysis of management problems</li>
    <li class="t field-item" style="left:437px;top:904px;">implementation of proposed solutions</li>
  </ul>
  <span class="t btn-label" style="left:84px;top:870px;">read<br>more</span>

  <h2 class="t title" style="left:86px;top:999px;">Get in <em>Touch</em></h2>
  <p class="t body-copy" style="left:86px;top:1062px;">krelto is always at your service.<br>Request a consultancy session<br>by either calling us or<br>filling out our query form.</p>
  <p class="t copyright" style="left:86px;top:1182px;">Copyright © 2013 krelto CONSULTANCY - All Rights Reserved</p>

  <form>
    <span class="t form-title" style="left:485px;top:983px;">QUERY FORM</span>
    <span class="field-box" style="top:1012px;">enter your email</span>
    <span class="field-box" style="top:1045px;">enter your phone</span>
    <span class="t privacy" style="left:562px;top:1080px;">your data is strictly private and will be used only for the above purpose.</span>
    <span class="t btn-label" style="left:565px;top:1140px;">submit</span>
  </form>
</div>
</body>
</html>
```